Business Card for boutique psychology business

Business card for boutique psychology practice in Melbourne. I want them to be relatively simply with the logo and backing colour taking up the front side. Then, text on the back, with my name; professional title (Clinical Psychologist); website - mirotherapy.com.au; email: hello@mirotherapy.com.au; insta: @miro.therapy.emdr
Back should also have the words: Listen. Restore. Grow
Fonts used for logo are: Mikea Demo and Gotham Medium. Use something for back text that will compliment these.
Brand colours uploaded below. I'd like to see options in both olive and blush.

```html
<!DOCTYPE html>
<html lang="en">
<head>
<meta charset="utf-8">
<title>miro therapy + EMDR — business cards</title>
<link rel="stylesheet" href="https://fonts.googleapis.com/css2?family=Montserrat:wght@300;400;500&display=swap">
<style>
  :root {
    --olive: #43452d;
    --blush: #eacfbe;
    --stage: #3a3a3a;
    --card-w: 520px;
    --card-h: 300px;
  }
  * { margin: 0; padding: 0; box-sizing: border-box; }
  html, body { width: 1200px; height: 689px; overflow: hidden; }
  body {
    background: var(--stage);
    font-family: "Montserrat", Arial, sans-serif;
    display: flex;
    align-items: center;
    justify-content: center;
    gap: 60px;
  }
  .card {
    position: relative;
    width: var(--card-w);
    height: var(--card-h);
    border-radius: 22px;
    overflow: hidden;
  }

  /* Front */
  .card--front {
    background: var(--olive);
    color: var(--blush);
    display: flex;
    flex-direction: column;
    align-items: center;
    justify-content: center;
  }
  .wordmark {
    display: flex;
    flex-direction: column;
    align-items: center;
    color: var(--blush);
    line-height: 1;
  }
  .wordmark__name { font-size: 104px; font-weight: 300; letter-spacing: -1px; }
  .wordmark__sub { font-size: 25px; font-weight: 500; margin-top: 6px; letter-spacing: 0.5px; }
  .tagline {
    margin-top: 34px;
    font-size: 12px;
    font-weight: 300;
    letter-spacing: 1px;
  }

  /* Back */
  .card--back { background: var(--blush); color: var(--olive); }
  .back__band { position: absolute; inset: 0; width: 100%; height: 100%; }
  .card--back .wordmark {
    position: absolute;
    top: 30px;
    right: 44px;
  }
  .card--back .wordmark__name { font-size: 64px; }
  .card--back .wordmark__sub { font-size: 15px; margin-top: 4px; }

  .contact {
    position: absolute;
    left: 34px;
    bottom: 28px;
    color: var(--olive);
  }
  .contact__name {
    font-size: 22px;
    font-weight: 300;
    letter-spacing: 2px;
    text-transform: uppercase;
  }
  .contact__title { font-size: 12.5px; font-weight: 400; margin: 2px 0 12px; }
  .contact__list { list-style: none; }
  .contact__item {
    display: flex;
    align-items: center;
    gap: 10px;
    font-size: 12.5px;
    line-height: 21px;
  }
  .contact__icon { width: 12px; height: 12px; flex: none; }
</style>
</head>
<body>

  <section class="card card--front" aria-label="Card front">
    <div class="wordmark">
      <span class="wordmark__name">miro</span>
      <span class="wordmark__sub">therapy + EMDR</span>
    </div>
    <p class="tagline">Listen. Restore. Grow</p>
  </section>

  <section class="card card--back" aria-label="Card back">
    <svg class="back__band" viewBox="0 0 520 300" preserveAspectRatio="none" aria-hidden="true">
      <path d="M190 0 C 250 115 400 165 520 128 L520 0 Z" fill="var(--olive)"/>
    </svg>

    <div class="wordmark">
      <span class="wordmark__name">miro</span>
      <span class="wordmark__sub">therapy + EMDR</span>
    </div>

    <div class="contact">
      <h1 class="contact__name">Daniel Hart</h1>
      <p class="contact__title">Clinical Psychologist</p>
      <ul class="contact__list">
        <li class="contact__item">
          <svg class="contact__icon" viewBox="0 0 24 24" aria-hidden="true"><path fill="var(--olive)" d="M6.6 10.8a15 15 0 0 0 6.6 6.6l2.2-2.2a1 1 0 0 1 1-.25 11.4 11.4 0 0 0 3.6.57 1 1 0 0 1 1 1V20a1 1 0 0 1-1 1A17 17 0 0 1 3 4a1 1 0 0 1 1-1h3.5a1 1 0 0 1 1 1c0 1.250.2 2.45.57 3.57a1 1 0 0 1-.25 1z"/></svg>
          (03) 555 0142
        </li>
        <li class="contact__item">
          <svg class="contact__icon" viewBox="0 0 24 24" aria-hidden="true"><rect x="2" y="5" width="20" height="14" rx="1.5" fill="var(--olive)"/><path d="M3 6l9 7 9-7" fill="none" stroke="var(--blush)" stroke-width="1.6"/></svg>
          hello@mirotherapy.com.au
        </li>
        <li class="contact__item">
          <svg class="contact__icon" viewBox="0 0 24 24" aria-hidden="true"><g fill="none" stroke="var(--olive)" stroke-width="2"><circle cx="12" cy="12" r="9.5"/><ellipse cx="12" cy="12" rx="4" ry="9.5"/><path d="M2.5 12h19"/></g></svg>
          www.mirotherapy.com.au
        </li>
        <li class="contact__item">
          <svg class="contact__icon" viewBox="0 0 24 24" aria-hidden="true"><circle cx="12" cy="12" r="9.5" fill="none" stroke="var(--olive)" stroke-width="2"/></svg>
          @miro.therapy.emdr
        </li>
      </ul>
    </div>
  </section>

</body>
</html>
```